Verpackungen für Sekt/Champagner Flaschen
Zielgruppe
Dekoration für Hochzeiten. Tisch Dekoration für Hochzeiten. Zielgruppe alles was mit Hochzeiten zutun hat
Aufgabenstellung
Wir lassen gerade ein Tube/Dose herstellen, die als Umverpackung oder einfach Verpackung für Sekt/Champagne Flaschen dienen soll die dann auf die Tische für Hochzeit´s Deko kommt um die die Tisch Deko aufzubessern, statt einfach nur eine Sekt Flasche stehen zu haben. .Die Tube wird komplett in weiß sein und alles andere an Design soll in einem Gold sein. Mr&Mrs oder Just Married mit Herzen und alles was sonst dazu gehört, da lassen wir freie Hand.
Das Design soll Schlicht sein aber auch Luxuriös.
Durchmesser der Tube wird 8,5 cm haben und 34-35 cm sein.
Die Goldene Schrift und das Muster soll am Ende in einem Relief Lack auf der Tube erscheinen

```html
<!DOCTYPE html>
<html lang="de">
<head>
<meta charset="utf-8">
<title>Just Married – Banderole</title>
<link rel="stylesheet" href="https://fonts.googleapis.com/css2?family=Yanone+Kaffeesatz:wght@400&display=swap">
<style>
  :root {
    --paper: #ffffff;
    --panel: #1f2521;
    --bronze: #a3825a;
    --gold: #b89260;
    --gold-light: #d2b07c;
    --gold-deep: #8a6a3e;
  }
  html, body {
    margin: 0;
    padding: 0;
    overflow: hidden;
    background: var(--paper);
  }
  .banderole {
    position: relative;
    width: 1200px;
    height: 292px;
    background: var(--paper);
    overflow: hidden;
  }
  .stripes {
    position: absolute;
    top: 131px;
    width: 411px;
  }
  .stripes--left { left: 0; }
  .stripes--right { left: 789px; width: 392px; }
  .stripes span {
    display: block;
    height: 10px;
    margin-bottom: 6px;
    background: var(--bronze);
  }
  .label {
    position: absolute;
    left: 439px;
    top: 46px;
    width: 322px;
    height: 203px;
    background: var(--panel);
  }
  .crown {
    position: absolute;
    left: 107px;
    top: 10px;
    width: 108px;
    height: 48px;
    border-radius: 6px 6px 2px 2px;
    background: linear-gradient(180deg, var(--gold-light), var(--gold-deep));
  }
  .laurel {
    position: absolute;
    top: 56px;
    width: 26px;
    height: 102px;
    border-radius: 50%;
    background: linear-gradient(180deg, var(--gold-light), var(--gold-deep));
  }
  .laurel--left { left: 41px; }
  .laurel--right { right: 41px; }
  .tagline {
    position: absolute;
    left: 0;
    right: 0;
    top: 78px;
    margin: 0;
    text-align: center;
    font-family: "Yanone Kaffeesatz", "Arial Narrow", sans-serif;
    font-weight: 400;
    font-size: 40px;
    line-height: 44px;
    color: var(--gold);
  }
</style>
</head>
<body>
  <div class="banderole">
    <div class="stripes stripes--left"><span></span><span></span><span></span></div>

    <div class="label">
      <div class="crown" role="img" aria-label="Goldene Krone als Ornament"></div>
      <div class="laurel laurel--left" role="img" aria-label="Goldener Lorbeerzweig links"></div>
      <div class="laurel laurel--right" role="img" aria-label="Goldener Lorbeerzweig rechts"></div>
      <p class="tagline">Just Married<br>with hearts</p>
    </div>

    <div class="stripes stripes--right"><span></span><span></span><span></span></div>
  </div>
</body>
</html>
```